Design a helpdesk ticketing platform *

We are launching a helpdesk ticketing platform. Very much like quellbox.com, merrylark.com, pivolta.com, brisktray.com etc. We have a full mid-fidelity prototype built and we want someone to build the full fidelity of the product.

You can view the full mid-fidelity prototype here: https://lnk.vexora.net/Qa8Lpw

The best way moving forward is to just design the following 4 pages

- Main Dashboard https://lnk.vexora.net/81hRtd
- All tickets https://lnk.vexora.net/jwNoEb
- Viewing a ticket https://lnk.vexora.net/Ys4VmK
- Contacts https://lnk.vexora.net/pHeXuo

Target Market(s)

Small business owners

Industry/Entity Type

Saas

Number of Pages Required

4 page

Font styles to use
Serif
Sans Serif

Colors

Designer to choose colors to be used in the design.

Requirements
Must have
• Must follow the prototype exactly. We are not looking for any UX changes. We want the designe xactly as the prototype is. We are only looking for design ideas.
Should not have
• modern, clean. We'd love to see the primary color as yellow, purple, orange, green or blue. You choose which one you think looks best and go with that.

```html
<!DOCTYPE html>
<html lang="en">
<head>
<meta charset="utf-8">
<title>deskwave · Dashboard</title>
<link href="https://fonts.googleapis.com/css2?family=Roboto:wght@400;500&family=Roboto+Condensed:wght@400;500&display=swap" rel="stylesheet">
<style>
:root{
  --navy:#063a66;
  --blue:#2f97e2;
  --sky:#1a9bf0;
  --red:#e02020;
  --green:#6ab51a;
  --orange:#f39200;
  --header-green:#1f5a12;
  --header-green-soft:#2a6a18;
  --page:#f5f5f5;
  --ink:#333;
  --muted:#666;
  --rule:#dcdcdc;
  --pink:#e8245a;
  --cyan:#21c1e0;
}
*{box-sizing:border-box;margin:0;padding:0}
html,body{width:1200px;height:1059px;overflow:hidden}
body{position:relative;background:var(--page);font-family:"Roboto",sans-serif;color:var(--ink)}
.sidebar{position:absolute;left:0;top:0;width:236px;height:1059px;background:var(--navy);color:#fff}
.profile{position:absolute;left:0;top:0;width:236px;height:162px;background:linear-gradient(180deg,var(--header-green-soft) 0%,var(--header-green) 100%)}
.brand{position:absolute;left:18px;top:16px;font-size:25px;letter-spacing:.5px}
.menu-icon{position:absolute;left:199px;top:22px}
.avatar{position:absolute;left:19px;top:81px;width:50px;height:50px;border-radius:50%;background:linear-gradient(#c9c9c9,#8d8d8d);border:2px solid #fff}
.user-name{position:absolute;left:76px;top:91px;font-size:21px}
.new-ticket{position:absolute;left:19px;top:184px;width:198px;height:31px;background:#fff;color:#555;font-size:13px;padding:7px 7px;letter-spacing:.4px}
.new-ticket i{position:absolute;right:7px;top:6px;width:4px;height:20px;background:radial-gradient(circle,#999 1.6px,transparent 2px) 0 0/4px 7px}
.nav-item{position:absolute;left:61px;font-size:13.5px;letter-spacing:.6px}
.nav-icon{position:absolute;left:21px}
.active-bar{position:absolute;left:18px;top:239px;width:199px;height:25px;background:var(--blue)}
.sub{position:absolute;left:78px;font-size:12.5px;letter-spacing:.3px}
.divider{position:absolute;left:69px;top:423px;width:136px;height:1px;background:#3b6590}
.caret{position:absolute;left:209px;width:0;height:0;border-left:4px solid transparent;border-right:4px solid transparent;border-top:5px solid #fff}
.topbar{position:absolute;left:236px;top:0;width:964px;height:58px;background:var(--blue);color:#fff}
.crumb{position:absolute;left:23px;top:22px;font-size:13px;letter-spacing:.6px}
.search{position:absolute;left:643px;top:15px;width:235px;height:22px;border-bottom:1px solid #fff}
.search .cursor{position:absolute;left:0;top:3px;width:1px;height:13px;background:#fff}
.search svg{position:absolute;right:0;top:-1px}
.greeting{position:absolute;left:257px;top:92px;font-size:26px;font-weight:400;color:#666;letter-spacing:.3px}
.greeting b{font-weight:400;color:#333}
.hr{position:absolute;left:236px;top:140px;width:964px;height:1px;background:#d6d6d6}
.stat{position:absolute;top:164px;width:134px;height:68px;color:#fff;font-family:"Roboto Condensed",sans-serif;padding:5px 7px;box-shadow:0 1px 3px rgba(0,0,0,.25)}
.stat .num{font-size:30px;line-height:32px}
.stat .lbl{font-size:15.5px}
.stat .lbl.strong{font-weight:500}
.section-bar{position:absolute;left:258px;top:257px;width:855px;height:42px;background:var(--blue);color:#fff;font-size:17.5px;letter-spacing:.5px;padding:11px 32px}
.card{position:absolute;left:258px;width:855px;background:#fff;box-shadow:0 1px 4px rgba(0,0,0,.22)}
.card h2{position:absolute;left:33px;top:28px;font-size:16px;font-weight:400;letter-spacing:.5px}
.card .rule{position:absolute;left:13px;right:15px;top:55px;height:1px;background:var(--rule)}
.timeline{position:absolute;left:39px;top:80px;width:1px;height:170px;background:#e2e2e2}
.event{position:absolute;left:57px;font-size:12.5px;letter-spacing:.3px;line-height:22px}
.dot{position:absolute;left:-26px;top:7px;width:9px;height:9px;border-radius:50%;border:2px solid var(--blue);background:#fff}
.dot.pink{border-color:var(--pink)}
.dot.cyan{border-color:var(--cyan)}
.load-more{position:absolute;left:595px;top:990px;width:182px;height:33px;background:var(--blue);color:#fff;font-size:12.5px;font-weight:500;letter-spacing:.6px;text-align:center;line-height:33px}
.toolbar{position:absolute;left:965px;top:1029px;width:235px;height:30px;background:#1d5a16;color:#fff;font-size:11.5px}
.toolbar .count{position:absolute;left:50px;top:8px;width:57px;height:15px;border:1px solid #7aa070;font-size:11px;display:flex;justify-content:space-around;line-height:13px}
.toolbar .label{position:absolute;left:112px;top:8px}
.toggle{position:absolute;left:176px;top:7px;width:46px;height:16px;border-radius:8px;background:#0e3a0b;font-size:9px;line-height:16px;padding-left:19px}
.toggle::before{content:"";position:absolute;left:1px;top:1px;width:14px;height:14px;border-radius:50%;background:#fff}
</style>
</head>
<body>
<aside class="sidebar">
  <div class="profile" role="img" aria-label="Decorative header background area"></div>
  <div class="brand">deskwave</div>
  <svg class="menu-icon" width="22" height="18" viewBox="0 0 22 18"><rect y="0" width="22" height="3" fill="#fff"/><rect y="7.5" width="22" height="3" fill="#fff"/><rect y="15" width="22" height="3" fill="#fff"/></svg>
  <div class="avatar" role="img" aria-label="User profile photo"></div>
  <div class="user-name">Marcus</div>

  <div class="new-ticket">New Ticket<i></i></div>

  <div class="active-bar"></div>
  <svg class="nav-icon" style="top:243px" width="22" height="17" viewBox="0 0 22 17"><path d="M2 15 A9 9 0 1 1 20 15" fill="none" stroke="#f2d21b" stroke-width="2"/><path d="M11 13 L16 6" stroke="#f2d21b" stroke-width="2"/></svg>
  <div class="nav-item" style="top:244px;left:60px">DASHBOARD</div>

  <svg class="nav-icon" style="top:277px" width="24" height="24" viewBox="0 0 24 24"><path d="M3 13 L13 3 L21 11 L11 21 Z" fill="none" stroke="#7ccf3a" stroke-width="1.5"/><path d="M9 9 L15 15" stroke="#7ccf3a" stroke-width="1.5" stroke-dasharray="2 2"/></svg>
  <div class="nav-item" style="top:282px">TICKETS</div>
  <div class="caret" style="top:288px"></div>
  <div class="sub" style="top:314px">All tickets</div>
  <div class="sub" style="top:340px">My tickets</div>
  <div class="sub" style="top:366px">Open tickets</div>
  <div class="sub" style="top:393px">Unassigned Tickets</div>
  <div class="divider"></div>
  <div class="sub" style="top:432px">Spam</div>
  <div class="sub" style="top:458px">Trash</div>

  <svg class="nav-icon" style="top:503px" width="14" height="15" viewBox="0 0 14 15"><circle cx="7" cy="4" r="3.6" fill="#7ccf3a"/><path d="M0 15 C0 8 14 8 14 15 Z" fill="#7ccf3a"/></svg>
  <div class="nav-item" style="top:503px">CONTACTS</div>

  <svg class="nav-icon" style="top:545px" width="15" height="15" viewBox="0 0 16 16"><circle cx="8" cy="8" r="5" fill="none" stroke="#8d8ff0" stroke-width="3" stroke-dasharray="2.2 1.6"/><circle cx="8" cy="8" r="2.2" fill="#8d8ff0"/></svg>
  <div class="nav-item" style="top:545px">ADMIN SETTINGS</div>
  <div class="caret" style="top:550px"></div>

  <svg class="nav-icon" style="top:585px" width="17" height="22" viewBox="0 0 17 22"><rect x="1" y="3" width="15" height="18" fill="none" stroke="#b8d62a" stroke-width="1.5"/><rect x="5" y="1" width="7" height="4" fill="#b8d62a"/><path d="M4 9h9M4 12h9M4 15h9M4 18h9" stroke="#b8d62a"/></svg>
  <div class="nav-item" style="top:589px">ACCOUNT &amp; BILLING</div>
</aside>

<header class="topbar">
  <div class="crumb">DASHBOARD</div>
  <div class="search"><span class="cursor"></span>
    <svg width="17" height="17" viewBox="0 0 17 17"><circle cx="7" cy="7" r="5.5" fill="none" stroke="#fff" stroke-width="2.2"/><path d="M11 11 L16 16" stroke="#fff" stroke-width="2.4"/></svg>
  </div>
</header>

<h1 class="greeting">Good Morning, <b>Marcus</b></h1>
<div class="hr"></div>

<div class="stat" style="left:259px;background:var(--sky)"><div class="num">16</div><div class="lbl strong">Open Tickets</div></div>
<div class="stat" style="left:403px;background:var(--red)"><div class="num">14</div><div class="lbl">Due Today</div></div>
<div class="stat" style="left:547px;background:var(--green)"><div class="num">14</div><div class="lbl">Unassigned</div></div>
<div class="stat" style="left:691px;background:var(--orange)"><div class="num">0</div><div class="lbl">Overdue</div></div>
<div class="stat" style="left:835px;background:var(--blue)"><div class="num">0</div><div class="lbl">On Hold</div></div>
<div class="stat" style="left:980px;background:var(--red)"><div class="num">11</div><div class="lbl strong">Not Resolved</div></div>

<div class="section-bar">Recent Activities</div>

<section class="card" style="top:325px;height:302px">
  <h2>Today</h2><div class="rule"></div>
  <div class="timeline"></div>
  <div class="event" style="top:65px"><span class="dot"></span>4.49 p.m<br>Pella Moor assigned forgot to cc, trying again (#15)to Dorian Vale</div>
  <div class="event" style="top:148px"><span class="dot pink"></span>10.30 a.m<br>Pella Moor assigned forgot to cc, trying again (#15)to Dorian Vale</div>
  <div class="event" style="top:232px"><span class="dot cyan"></span>10.30 a.m<br>Pella Moor assigned forgot to cc, trying again (#15)to Dorian Vale</div>
</section>

<section class="card" style="top:652px;height:307px">
  <h2>Yesterday</h2><div class="rule" style="top:57px"></div>
  <div class="timeline"></div>
  <div class="event" style="top:73px"><span class="dot"></span>4.49 p.m<br>Pella Moor assigned forgot to cc, trying again (#15)to Dorian Vale</div>
  <div class="event" style="top:155px"><span class="dot pink"></span>10.30 a.m<br>Pella Moor assigned forgot to cc, trying again (#15)to Dorian Vale</div>
  <div class="event" style="top:239px"><span class="dot cyan"></span>10.30 a.m<br>Pella Moor assigned forgot to cc, trying again (#15)to Dorian Vale</div>
</section>

<div class="load-more">LOAD MORE</div>

<div class="toolbar">
  <svg style="position:absolute;left:10px;top:5px" width="32" height="21" viewBox="0 0 32 21"><g fill="#fff"><rect x="0" y="0" width="5" height="5"/><rect x="8" y="0" width="5" height="5"/><rect x="16" y="0" width="5" height="5"/><rect x="0" y="8" width="5" height="5"/><rect x="8" y="8" width="5" height="5"/><rect x="16" y="8" width="5" height="5"/><rect x="0" y="16" width="5" height="5"/><rect x="8" y="16" width="5" height="5"/><rect x="16" y="16" width="5" height="5"/><path d="M26 10 L29 6 L32 10 Z"/></g></svg>
  <div class="count"><span>0</span><span>/</span><span>0</span></div>
  <div class="label">Comments</div>
  <div class="toggle">OFF</div>
</div>
</body>
</html>
```